Pitch Deck Design for Startup (Quorvo.io)

Graphic Design for Pitch Deck [Pitch Deck content in links below]

Who are we ?

“Quorvo” always, never “QUORVO”

Quorvo is an platform to easily use & publish algorithms with minimal effort.

Algorithms include:
Artificial Intelligence
Deep Learning
Machine Learning

No matter what type of applications or software users have, they can implement any of our State-of-Art AI algorithms in their apps with 3 lines of code.

Quorvo is untangling the hard parts™

Using Quorvo is as easy as just 3 lines of code to be up and running in minutes.

The general idea is that there's a central place for any app to find great algorithms when they want to use AI algorithms/models and implement them with extreme ease and speed, and this place is Quorvo.io.

For the information this deck needs to contain, please refer to this google slide: http://lnkshrt.example/7Tq9Wz, all the information in there are necessary, we need you to transform this deck into a much better looking, clear, colorful, and also stylish & concise deck. If you can give it a bit of Sci-Fi style would be great as well (not a must have)!

You have total freedom to design however you want, just remember three principles:

It needs to establish the brand / image of the Quorvo platform to the description above.

Our audience is wide - so use the ‘explain it like I am 5 year-old’ principle.

DO NOT assume specialist knowledge in the audience - make the deck extremely simple, clear, intuitive and compelling!
If there’s something you’re not sure about in the deck, anything, please don’t hesitate to ask us to get it right!!!

In terms of styles, what we like is something fun & modern but doesn’t lose a sense of quality (seriousness).

We want a clear storyline, and the current sequence and the way we organise the info is what we think is good, but it might not be the best way to present in the deck… additional slide ideas can be submitted with in the process.

QUESTIONS? If you have any questions or better suggestions on ANYTHING related to the deck, feel free to let us know at a@quorvo.io, we normally respond promptly.

The design of our website uses more than one colors, and it has slight movement when people scrolling as well. Something goes along with its design would be a nice attribute (Note: not a must have, feel free to design your way, if you try to go along with those colors but the deck doesn’t look good, the design would have a very low chance of being selected). Please take a look for your inspirations: http://quorvo.io.

Again, any questions, and enquiries, feel free to reach out to us: a@quorvo.io

Target Market(s)

Angel Investors (Tech Startups), Developers, Software Companies

Industry/Entity Type

Startup

Font styles to use
Serif

Requirements
Must have
• GOOD DECKS EXAMPLES:
• For your reference, here are some deck designs we like:
• Zelko, NestLoop, Palbridge
• http://lnkshrt.example/4Hd2Kp. The reason is: they are simple, clean, right on target, they used very simple but very friendly & nice colors. On every slide, the audience can kinda get the idea at the very first glance.
Nice to have
• If you can use multiple colors (themed in our style) , that would be awesome!
Should not have
• BAD DECKS EXAMPLES:
• The ones we don’t like: http://lnkshrt.example/9Rb6Nm, http://lnkshrt.example/3Fx8Jv. The reason? These are very tedious, not intuitive, and the design is very old fashioned. The information design of the deck is not giving great intuitions at the first sight, the audience has to go through all the text to get the idea.

```html
<!DOCTYPE html>
<html lang="en">
<head>
<meta charset="utf-8">
<title>Quorvo Pitch Deck</title>
<link rel="stylesheet" href="https://fonts.googleapis.com/css2?family=Montserrat:wght@400;500;600;700;800&family=Exo+2:wght@400;500&display=swap">
<style>
  :root {
    --page: #ececec;
    --ink: #0a0a0a;
    --white: #ffffff;
    --purple-deep: #2c1660;
    --purple-mid: #3a1f78;
    --purple-soft: #5a3aa8;
    --lilac: #c9a6f0;
    --sky: #4fb8ea;
    --sky-light: #5ec8f2;
    --teal: #1fd1a8;
    --violet: #7c6fe0;
    --navy: #1d2744;
    --peach: #f6c99a;
    --heading: "Montserrat", sans-serif;
    --display: "Exo 2", sans-serif;
  }
  html, body {
    margin: 0;
    width: 1200px;
    height: 1200px;
    overflow: hidden;
    background: var(--page);
  }
  .deck { position: relative; width: 1200px; height: 1200px; }
  .slide {
    position: absolute;
    display: block;
    box-shadow: 0 2px 6px rgba(0,0,0,.12);
  }
  .slide--cover { left: 280px; top: 24px; width: 640px; height: 360px; }
  .slide--trend { left: 30px; top: 411px; width: 546px; height: 307px; }
  .slide--problem { left: 612px; top: 411px; width: 546px; height: 307px; }
  .slide--meanwhile { left: 30px; top: 746px; width: 546px; height: 307px; }
  .slide--solution { left: 612px; top: 746px; width: 546px; height: 307px; }
  .heading { font-family: var(--heading); font-weight: 500; fill: var(--white); font-size: 30px; letter-spacing: -0.5px; }
  .brand-small { font-family: var(--heading); font-weight: 700; font-size: 12px; fill: var(--white); }
  .label { font-family: var(--heading); font-weight: 600; font-size: 10.5px; fill: var(--white); }
  .body { font-family: var(--heading); font-weight: 400; font-size: 7.6px; fill: var(--white); }
  .body--blue { fill: var(--sky-light); }
  .page-no { font-family: var(--heading); font-weight: 600; font-size: 11px; fill: var(--navy); }
  .display { font-family: var(--display); }
</style>
</head>
<body>
<main class="deck">

  <!-- Cover -->
  <svg class="slide slide--cover" viewBox="0 0 800 450" aria-label="Cover slide">
    <defs>
      <linearGradient id="photoTone" x1="0" y1="0" x2="1" y2="0.3">
        <stop offset="0" stop-color="#eef0f3"/>
        <stop offset="0.5" stop-color="#4a4f58"/>
        <stop offset="1" stop-color="#1c1f26"/>
      </linearGradient>
      <linearGradient id="brandLine" x1="0" x2="1">
        <stop offset="0" stop-color="#4fb8ea"/>
        <stop offset="1" stop-color="#c9a6f0"/>
      </linearGradient>
    </defs>
    <rect width="800" height="450" fill="var(--white)"/>
    <rect x="240" y="0" width="560" height="350" fill="url(#photoTone)" role="img" aria-label="Photo of a developer with headphones coding at multiple monitors"/>
    <polygon points="240,0 390,0 630,350 240,350" fill="var(--white)" opacity="0.88"/>
    <polygon points="0,0 240,0 240,350 0,350" fill="var(--white)"/>
    <text x="60" y="240" font-family="Montserrat, sans-serif" font-weight="800" font-size="96" fill="var(--ink)" letter-spacing="-2">Quorvo</text>
    <rect x="0" y="350" width="630" height="7" fill="url(#brandLine)"/>
    <polygon points="0,357 630,357 680,450 0,450" fill="var(--ink)"/>
    <polygon points="625,313 800,313 800,450 680,450 630,357" fill="var(--teal)"/>
    <polygon points="0,396 50,396 78,450 0,450" fill="var(--sky)"/>
    <text x="160" y="414" class="display" font-size="26" fill="var(--white)" letter-spacing="0.5">AI Anywhere, Anytime</text>
    <text x="710" y="409" font-family="Montserrat, sans-serif" font-size="10" fill="var(--navy)">Aug 2018</text>
  </svg>

  <!-- Everyone wants AI -->
  <svg class="slide slide--trend" viewBox="0 0 682 383" aria-label="Everyone wants AI">
    <defs>
      <linearGradient id="underline" x1="0" x2="1">
        <stop offset="0" stop-color="#4fb8ea"/>
        <stop offset="1" stop-color="#c9a6f0"/>
      </linearGradient>
    </defs>
    <rect width="682" height="383" fill="var(--purple-deep)"/>
    <polygon points="0,383 0,230 120,383" fill="var(--purple-mid)"/>
    <polygon points="250,0 682,0 682,383 560,383" fill="var(--purple-mid)" opacity="0.7"/>
    <polygon points="600,383 682,260 682,383" fill="var(--purple-soft)" opacity="0.6"/>
    <text x="40" y="52" class="heading">EVERYONE WANTS AI</text>
    <rect x="40" y="67" width="66" height="2" fill="url(#underline)"/>
    <text x="625" y="36" class="brand-small">Quorvo</text>
    <polyline fill="none" stroke="var(--white)" stroke-width="2" stroke-linejoin="round"
      points="74,256 87,250 99,245 111,253 123,259 135,252 147,250 159,254 171,247 183,256 195,260 208,265 220,263 232,258 244,260 256,257 268,256 281,256 293,264 305,271 317,265 330,259 342,255 355,252 367,246 379,246 391,251 403,257 415,244 427,240 439,234 451,223 457,196 466,210 476,195 488,217 498,220 505,192 515,172 526,146 534,125 541,106 550,92 558,102 566,95 574,118 582,95"/>
    <g fill="var(--white)">
      <circle cx="74" cy="256" r="2"/><circle cx="99" cy="245" r="2"/><circle cx="123" cy="259" r="2"/><circle cx="147" cy="250" r="2"/><circle cx="171" cy="247" r="2"/><circle cx="195" cy="260" r="2"/><circle cx="220" cy="263" r="2"/><circle cx="244" cy="260" r="2"/><circle cx="268" cy="256" r="2"/><circle cx="293" cy="264" r="2"/><circle cx="317" cy="265" r="2"/><circle cx="342" cy="255" r="2"/><circle cx="367" cy="246" r="2"/><circle cx="391" cy="251" r="2"/><circle cx="415" cy="244" r="2"/><circle cx="439" cy="234" r="2"/><circle cx="457" cy="196" r="2"/><circle cx="476" cy="195" r="2"/><circle cx="498" cy="220" r="2"/><circle cx="515" cy="172" r="2"/><circle cx="534" cy="125" r="2"/><circle cx="550" cy="92" r="2"/><circle cx="566" cy="95" r="2"/><circle cx="582" cy="95" r="2"/>
    </g>
    <text x="75" y="341" font-family="Montserrat, sans-serif" font-size="9.5" font-weight="600" text-decoration="underline"><tspan fill="#3a7bff" font-weight="400">Source</tspan><tspan fill="var(--white)">: Searchpulse trend</tspan></text>
    <polygon points="636,350 682,350 682,383 652,383" fill="var(--sky)"/>
    <text x="660" y="371" class="page-no">2</text>
  </svg>

  <!-- But -->
  <svg class="slide slide--problem" viewBox="0 0 682 383" aria-label="Problems with AI today">
    <rect width="682" height="383" fill="var(--purple-deep)"/>
    <polygon points="0,383 0,230 120,383" fill="var(--purple-mid)"/>
    <polygon points="250,0 682,0 682,383 560,383" fill="var(--purple-mid)" opacity="0.7"/>
    <polygon points="600,383 682,260 682,383" fill="var(--purple-soft)" opacity="0.6"/>
    <text x="40" y="52" class="heading">BUT</text>
    <rect x="40" y="67" width="66" height="2" fill="url(#underline)"/>
    <text x="625" y="36" class="brand-small">Quorvo</text>

    <line x1="158" y1="216" x2="499" y2="216" stroke="var(--lilac)" stroke-width="3"/>
    <g stroke="var(--white)" stroke-width="3" fill="var(--purple-deep)">
      <circle cx="158" cy="216" r="33"/><circle cx="273" cy="216" r="33"/><circle cx="386" cy="216" r="33"/><circle cx="499" cy="216" r="33"/>
    </g>
    <g fill="var(--white)" opacity="0.9">
      <circle cx="158" cy="216" r="26" role="img" aria-label="Icon: group of people with a star"/>
      <circle cx="273" cy="216" r="26" role="img" aria-label="Icon: code window with connections"/>
      <circle cx="386" cy="216" r="26" role="img" aria-label="Icon: person with a lightbulb"/>
      <circle cx="499" cy="216" r="26" role="img" aria-label="Icon: person working at a computer"/>
    </g>

    <text x="110" y="137" class="label">Rare Talents</text>
    <circle cx="113" cy="149" r="1.3" fill="var(--white)"/>
    <text class="body"><tspan x="130" y="154">Well trained AI talents</tspan><tspan x="130" y="164">are really hard to find.</tspan></text>

    <text x="316" y="100" class="label">Steep Learning Curve</text>
    <circle cx="319" cy="115" r="1.3" fill="var(--white)"/>
    <circle cx="319" cy="146" r="1.3" fill="var(--white)"/>
    <text class="body"><tspan x="335" y="120">AI takes a long time to learn,</tspan><tspan x="335" y="130">it's hard for normal developers</tspan><tspan x="335" y="140">to develop AI.</tspan><tspan x="335" y="151">Even slightly customising &amp;</tspan><tspan x="335" y="161">modifying AI algorithms can be</tspan><tspan x="335" y="171">challenging.</tspan></text>

    <text x="210" y="269" class="label">Long Dev Process</text>
    <circle cx="212" cy="288" r="1.3" fill="var(--white)"/>
    <circle cx="212" cy="319" r="1.3" fill="var(--white)"/>
    <text class="body"><tspan x="228" y="293">Finding the right AI solution &amp;</tspan><tspan x="228" y="303">AI development are time</tspan><tspan x="228" y="313">consuming.</tspan><tspan x="228" y="324">Infrastructures need to be very</tspan><tspan x="228" y="334">well configured for the best</tspan><tspan x="228" y="344">performance.</tspan></text>

    <text x="455" y="269" class="label">Repeated Works</text>
    <circle cx="457" cy="288" r="1.3" fill="var(--white)"/>
    <text class="body"><tspan x="474" y="293">Most people are re-training the</tspan><tspan x="474" y="303">same/very similar AI models</tspan><tspan x="474" y="313">and hosting them separately</tspan><tspan x="474" y="323">for use.</tspan></text>

    <polygon points="636,350 682,350 682,383 652,383" fill="var(--sky)"/>
    <text x="660" y="371" class="page-no">3</text>
  </svg>

  <!-- Meanwhile -->
  <svg class="slide slide--meanwhile" viewBox="0 0 682 383" aria-label="Meanwhile">
    <rect width="682" height="383" fill="var(--purple-deep)"/>
    <polygon points="0,383 0,230 120,383" fill="var(--purple-mid)"/>
    <polygon points="250,0 682,0 682,383 560,383" fill="var(--purple-mid)" opacity="0.7"/>
    <polygon points="600,383 682,260 682,383" fill="var(--purple-soft)" opacity="0.6"/>
    <text x="40" y="52" class="heading">MEANWHILE</text>
    <rect x="40" y="67" width="66" height="2" fill="url(#underline)"/>
    <text x="600" y="36" class="brand-small">Quorvo</text>

    <path d="M67,137 V120 Q67,112 75,112 H218 Q226,112 226,120 V137 Z" fill="var(--ink)"/>
    <text x="146" y="128" text-anchor="middle" class="label" font-size="10" fill="var(--sky-light)" style="fill:var(--sky-light)">AI Algorithmic Interests</text>
    <line x1="122" y1="143" x2="166" y2="143" stroke="var(--sky-light)" stroke-width="1.3" stroke-dasharray="4 2"/>
    <path d="M416,137 V120 Q416,112 424,112 H567 Q575,112 575,120 V137 Z" fill="var(--ink)"/>
    <text x="495" y="128" text-anchor="middle" class="label" font-size="10">AI Algorithmic Interests</text>
    <line x1="474" y1="143" x2="518" y2="143" stroke="var(--white)" stroke-width="1.3" stroke-dasharray="4 2"/>

    <g fill="none" stroke="var(--white)" stroke-width="0.9">
      <circle cx="80" cy="167" r="2.6"/><circle cx="80" cy="188" r="2.6"/><circle cx="80" cy="208" r="2.6"/>
      <circle cx="425" cy="167" r="2.6"/><circle cx="425" cy="198" r="2.6"/>
    </g>
    <text class="body body--blue"><tspan x="94" y="170">AI has been proven to deliver great</tspan><tspan x="94" y="180">results.</tspan><tspan x="94" y="190">Digital products are (looking for)</tspan><tspan x="94" y="200">implementing AI in software.</tspan><tspan x="94" y="211">AI has already became the "Next Big</tspan><tspan x="94" y="221">Thing".</tspan></text>
    <text class="body"><tspan x="440" y="170">Most sophisticated digital products are</tspan><tspan x="440" y="180">heavily relying on APIs to interconnect</tspan><tspan x="440" y="190">components &amp; integrate w/ services.</tspan><tspan x="440" y="200">APIs are turning the world into a giant</tspan><tspan x="440" y="210">computer.</tspan></text>

    <polyline points="150,245 150,296 240,296" fill="none" stroke="var(--sky-light)" stroke-width="1.3"/>
    <polygon points="242,296 235,293 235,299" fill="var(--sky-light)"/>
    <polyline points="514,245 514,290 432,290" fill="none" stroke="var(--white)" stroke-width="1.3"/>
    <polygon points="429,290 436,287 436,293" fill="var(--white)"/>

    <polyline points="276,311 340,266 363,295 398,261" fill="none" stroke="var(--white)" stroke-width="1.5"/>
    <polyline points="275,287 310,295 338,290 365,264 398,305" fill="none" stroke="var(--sky-light)" stroke-width="1.5"/>
    <g fill="var(--purple-deep)" stroke-width="1.5">
      <circle cx="276" cy="311" r="3.5" stroke="var(--white)"/><circle cx="340" cy="266" r="3.5" stroke="var(--white)"/><circle cx="363" cy="295" r="3.5" stroke="var(--white)"/><circle cx="398" cy="261" r="3.5" stroke="var(--white)"/>
      <circle cx="275" cy="287" r="3.5" stroke="var(--sky-light)"/><circle cx="310" cy="295" r="3.5" stroke="var(--sky-light)"/><circle cx="365" cy="264" r="3.5" stroke="var(--sky-light)"/><circle cx="398" cy="305" r="3.5" stroke="var(--sky-light)"/>
    </g>
    <text x="344" y="342" text-anchor="middle" class="display" font-size="17" fill="var(--white)">Are Biggest Tech Trends</text>

    <polygon points="636,350 682,350 682,383 652,383" fill="var(--sky)"/>
    <text x="660" y="371" class="page-no">4</text>
  </svg>

  <!-- Solution -->
  <svg class="slide slide--solution" viewBox="0 0 682 383" aria-label="Quorvo solution">
    <defs>
      <linearGradient id="leftFade" x1="0" y1="0" x2="1" y2="1">
        <stop offset="0" stop-color="#dbeafc"/>
        <stop offset="1" stop-color="#ffffff"/>
      </linearGradient>
      <linearGradient id="rightFade" x1="1" y1="0" x2="0" y2="1">
        <stop offset="0" stop-color="#e6dcfa"/>
        <stop offset="1" stop-color="#ffffff"/>
      </linearGradient>
      <linearGradient id="headlineTone" x1="0" x2="1">
        <stop offset="0" stop-color="#7b6fe0"/>
        <stop offset="1" stop-color="#8a80e8"/>
      </linearGradient>
    </defs>
    <rect width="682" height="383" fill="var(--white)"/>
    <polygon points="0,383 0,80 195,0 0,383" fill="url(#leftFade)" opacity="0.8"/>
    <polygon points="0,383 195,0 260,0 60,383" fill="url(#leftFade)" opacity="0.5"/>
    <polygon points="450,0 682,0 682,383" fill="url(#rightFade)" opacity="0.8"/>
    <polygon points="682,250 682,383 600,383" fill="#d9d3f7" opacity="0.6"/>
    <text x="625" y="36" class="brand-small" style="fill:var(--violet)">Quorvo</text>

    <text x="332" y="72" text-anchor="middle" font-family="Montserrat, sans-serif" font-weight="700" font-size="24" fill="var(--violet)">Quorvo</text>
    <text x="332" y="104" text-anchor="middle" font-family="Montserrat, sans-serif" font-weight="500" font-size="10.5" fill="var(--navy)">AI Algorithmic Marketplace</text>

    <rect x="273" y="133" width="119" height="37" rx="11" fill="var(--navy)" stroke="var(--lilac)" stroke-width="2.5"/>
    <text x="332" y="156" text-anchor="middle" font-family="Montserrat, sans-serif" font-weight="500" font-size="13" fill="var(--white)">Signup / in</text>
    <rect x="308" y="160" width="38" height="62" rx="8" fill="var(--peach)" role="img" aria-label="Illustration of a hand pointing at the button"/>

    <g font-family="Montserrat, sans-serif" font-size="10" fill="var(--navy)" text-anchor="middle">
      <text x="195" y="254">Best algorithm</text>
      <text x="260" y="254">|</text>
      <text x="343" y="254">Lightning speed</text>
      <text x="420" y="254">|</text>
      <text x="497" y="254">minimum efforts</text>
    </g>
    <rect x="65" y="277" width="536" height="2" fill="url(#underline)"/>
    <text x="338" y="320" text-anchor="middle" class="display" font-size="21" fill="var(--ink)">So We Give Everyone Instant Access To</text>
    <text x="338" y="360" text-anchor="middle" class="display" font-weight="500" font-size="36" fill="url(#headlineTone)">State-of-art Algorithms</text>

    <polygon points="636,350 682,350 682,383 652,383" fill="var(--sky)"/>
    <text x="660" y="371" class="page-no">5</text>
  </svg>

</main>
</body>
</html>
```